Business Card Design Project

Hello
I want a Simple Business card that uses the company logo that is easily reasonable but looks professional as I am an IT Services company and would look to share these cards with prospective clients.
The details are:
Kelvo Ridge Solutions
14 Marlow Crescent
Birmingham
B7 4QT
Telephone 0845 271 6049
I would like my name Gareth Wilcombe and my title Director on the card.
Target Market(s)
IT Professionals
Industry/Entity Type
Business

```html
<!DOCTYPE html>
<html lang="en">
<head>
<meta charset="utf-8">
<title>Kelvo Ridge Solutions – Business Card</title>
<link href="https://fonts.googleapis.com/css2?family=Open+Sans:wght@400;600&display=swap" rel="stylesheet">
<style>
  :root {
    --backdrop: #e9e9e6;
    --card-white: #ffffff;
    --card-shade: #f1f1f1;
    --green-dark: #4fb41a;
    --green-mid: #62c824;
    --green-light: #82dc3e;
    --title-yellow: #f3ea3c;
    --brand-grey: #3f3f3f;
    --brand-dot: #9fd46a;
    --text-white: #ffffff;
  }
  * { margin: 0; padding: 0; box-sizing: border-box; }
  html, body {
    width: 1200px;
    height: 1021px;
    overflow: hidden;
    background: var(--backdrop);
    font-family: "Open Sans", Arial, sans-serif;
  }
  .business-card {
    position: absolute;
    left: 150px;
    top: 253px;
    width: 900px;
    height: 514px;
    border-radius: 26px;
    overflow: hidden;
    background: linear-gradient(180deg, var(--card-white) 0%, var(--card-shade) 100%);
    box-shadow: 0 14px 34px rgba(0,0,0,0.18);
  }
  .brand {
    position: absolute;
    top: 0;
    left: 0;
    width: 100%;
    height: 262px;
    display: flex;
    align-items: center;
    justify-content: center;
    gap: 22px;
  }
  .brand-dot {
    width: 70px;
    height: 70px;
    border-radius: 50%;
    background: var(--brand-dot);
  }
  .brand-name {
    font-weight: 600;
    font-size: 50px;
    color: var(--brand-grey);
    letter-spacing: -0.5px;
  }
  .info-band {
    position: absolute;
    left: 0;
    bottom: 0;
    width: 100%;
    height: 252px;
    background: linear-gradient(100deg, var(--green-dark) 0%, var(--green-mid) 45%, var(--green-light) 60%, var(--green-mid) 75%, var(--green-dark) 100%);
    color: var(--text-white);
  }
  .person {
    position: absolute;
    left: 50px;
    bottom: 46px;
  }
  .person-title {
    display: block;
    margin-left: 190px;
    font-size: 34px;
    color: var(--title-yellow);
    line-height: 1.1;
  }
  .person-name {
    display: block;
    font-size: 46px;
    line-height: 1.2;
  }
  .contact {
    position: absolute;
    right: 60px;
    top: 38px;
    list-style: none;
    font-size: 27px;
    line-height: 1.3;
  }
  .contact-item {
    display: flex;
    align-items: center;
    gap: 20px;
    margin-bottom: 14px;
  }
  .contact-icon { width: 30px; height: 36px; flex: none; }
</style>
</head>
<body>
  <section class="business-card">
    <header class="brand">
      <span class="brand-dot"></span>
      <span class="brand-name">Kelvo Ridge Solutions</span>
    </header>
    <div class="info-band">
      <ul class="contact">
        <li class="contact-item">
          <svg class="contact-icon" viewBox="0 0 30 36" aria-hidden="true">
            <path d="M15 1C7.8 1 2 6.6 2 13.6 2 23 15 35 15 35s13-12 13-21.4C28 6.6 22.2 1 15 1z" fill="#fff"/>
            <circle cx="15" cy="13.5" r="5" fill="var(--green-mid)"/>
          </svg>
          <span>14 Marlow Crescent<br>Birmingham, B7 4QT</span>
        </li>
        <li class="contact-item">
          <svg class="contact-icon" viewBox="0 0 30 36" aria-hidden="true">
            <path d="M8 4c2-1 3 0 4 2l2 5c.5 1.5 0 2.5-1.2 3.3l-1.6 1c1.4 3.3 3.6 5.8 6.6 7.6l1.2-1.4c1-1.1 2-1.3 3.3-.6l4.4 2.6c1.8 1 2.1 2.2 1 3.8-1.8 2.8-4.6 3.8-7.7 2.6C11.5 27.6 5.6 20.7 3.6 12.4 2.9 8.9 4.6 5.8 8 4z" fill="#fff"/>
          </svg>
          <span>0845 271 6049</span>
        </li>
      </ul>
      <div class="person">
        <span class="person-title">Director</span>
        <span class="person-name">Gareth Wilcombe</span>
      </div>
    </div>
  </section>
</body>
</html>
```